Modern Design Business Card industrial maintenance company

Business card design for Company named Brookvale Equipment Services

Target Market(s)

Industrial

Industry/Entity Type

Maintenance and repair

Contact Information for Business Card

Place holder for address, office phone, mobile number and email

Requirements
Must have
• Clean modern look
Nice to have
• N/a

```html
<!DOCTYPE html>
<html lang="en">
<head>
<meta charset="utf-8">
<title>Brookvale Equipment Services – Business Card</title>
<link href="https://fonts.googleapis.com/css2?family=Orbitron:wght@600&family=Poppins:wght@400&display=swap" rel="stylesheet">
<style>
  :root {
    --backdrop: #c4c4c4;
    --ink: #000000;
    --paper: #ffffff;
    --card-w: 760px;
    --card-h: 435px;
  }
  * { box-sizing: border-box; margin: 0; padding: 0; }
  html, body {
    width: 1200px;
    height: 1146px;
    overflow: hidden;
    background: var(--backdrop);
  }
  .canvas {
    width: 1200px;
    height: 1146px;
    display: flex;
    flex-direction: column;
    align-items: center;
    justify-content: center;
    gap: 64px;
  }
  .card {
    position: relative;
    width: var(--card-w);
    height: var(--card-h);
    overflow: hidden;
  }

  /* Front */
  .card--front { background: var(--ink); color: var(--paper); }
  .brand {
    position: absolute;
    left: 125px;
    top: 159px;
    display: flex;
    align-items: center;
    gap: 26px;
  }
  .brand__ring {
    width: 118px;
    height: 118px;
    border: 5px solid var(--paper);
    border-radius: 50%;
    flex: none;
  }
  .brand__name {
    font-family: "Orbitron", sans-serif;
    font-weight: 600;
    color: var(--paper);
    line-height: 1;
  }
  .brand__name-main {
    display: block;
    font-size: 37px;
    letter-spacing: 2px;
  }
  .brand__name-sub {
    display: block;
    margin-top: 8px;
    font-size: 12.5px;
    letter-spacing: 6.2px;
  }

  /* Back */
  .card--back { background: var(--paper); color: var(--ink); }
  .company {
    position: absolute;
    left: 52px;
    top: 64px;
    width: 296px;
    padding-bottom: 6px;
    border-bottom: 3px solid var(--ink);
    font-family: "Orbitron", sans-serif;
    font-weight: 600;
    font-size: 21px;
    line-height: 1.15;
  }
  .contact {
    position: absolute;
    right: 44px;
    top: 160px;
    list-style: none;
    font-family: "Poppins", sans-serif;
    font-size: 16px;
    text-align: right;
  }
  .contact__item {
    display: flex;
    align-items: center;
    justify-content: flex-end;
    gap: 9px;
    height: 26px;
    margin-bottom: 8px;
    white-space: nowrap;
  }
  .contact__icon { width: 11px; height: 11px; flex: none; }
  .card__rule {
    position: absolute;
    left: 0;
    right: 0;
    top: 392px;
    height: 6px;
    background: var(--ink);
  }
</style>
</head>
<body>
<main class="canvas">
  <section class="card card--front" aria-label="Business card front">
    <div class="brand">
      <div class="brand__ring" aria-hidden="true"></div>
      <div class="brand__name">
        <span class="brand__name-main">BROOKVALE</span>
        <span class="brand__name-sub">EQUIPMENT SERVICES</span>
      </div>
    </div>
  </section>

  <section class="card card--back" aria-label="Business card back">
    <h1 class="company">Brookvale Equipment<br>Services</h1>
    <ul class="contact">
      <li class="contact__item">Office: +1 555 014 2200
        <svg class="contact__icon" viewBox="0 0 12 12" aria-hidden="true"><path d="M2.2 0.8 L4.4 0.8 L5.2 3.4 L3.8 4.6 C4.6 6.2 5.8 7.4 7.4 8.2 L8.6 6.8 L11.2 7.6 L11.2 9.8 C11.2 10.6 10.6 11.2 9.8 11.2 C5 11 1 7 0.8 2.2 C0.8 1.4 1.4 0.8 2.2 0.8 Z" fill="#000"/></svg>
      </li>
      <li class="contact__item">Mobile: +1 555 014 2290
        <svg class="contact__icon" viewBox="0 0 12 12" aria-hidden="true"><rect x="3" y="0.8" width="6" height="10.4" rx="1" fill="none" stroke="#000" stroke-width="1.2"/></svg>
      </li>
      <li class="contact__item">info@brookvaleequipment.com
        <svg class="contact__icon" viewBox="0 0 12 12" aria-hidden="true"><rect x="0.5" y="2.5" width="11" height="7.5" fill="#000"/><path d="M0.8 3 L6 7 L11.2 3" fill="none" stroke="#fff" stroke-width="0.9"/></svg>
      </li>
      <li class="contact__item">www.brookvaleequipment.com
        <svg class="contact__icon" viewBox="0 0 12 12" aria-hidden="true"><circle cx="6" cy="6" r="5" fill="#000"/><path d="M1 6 H11 M6 1 V11 M6 1 C3.5 4 3.5 8 6 11 M6 1 C8.5 4 8.5 8 6 11" fill="none" stroke="#fff" stroke-width="0.7"/></svg>
      </li>
      <li class="contact__item">210 Harlow Park Rd, Brookvale, OH 44102
        <svg class="contact__icon" viewBox="0 0 12 12" aria-hidden="true"><path d="M6 11.5 C6 11.5 1.8 7 1.8 4.4 C1.8 2.1 3.7 0.5 6 0.5 C8.3 0.5 10.2 2.1 10.2 4.4 C10.2 7 6 11.5 6 11.5 Z" fill="#000"/><circle cx="6" cy="4.4" r="1.6" fill="#fff"/></svg>
      </li>
    </ul>
    <div class="card__rule" aria-hidden="true"></div>
  </section>
</main>
</body>
</html>
```